Stationary Set for Morvale Telecom
Business card, Letterhead and Envenlope
Stationary Set for Morvale Telecom - Telecommunications
Creative Brief
Professional
Colin Pradwell
Managing Partner
87 Larkmont Suite:2261 NY, NY 10017
cp@morvaletel.com
www.morvaletel.com
Use the logo as an abstract background, Make it nice and clean. Blue white grey black are good color combos
www.morvaletel.com on the back of the business card

```html
<!DOCTYPE html>
<html lang="en">
<head>
<meta charset="utf-8">
<title>Morvale Telecom Stationery Set</title>
<link href="https://fonts.googleapis.com/css2?family=Open+Sans:wght@400;700&display=swap" rel="stylesheet">
<style>
  :root {
    --navy: #0d2a5c;
    --blue: #1f4f9a;
    --sky: #6f93c9;
    --mist: #e6ecf5;
    --paper: #ffffff;
    --ink: #1a1a1a;
    --grey: #7a7f88;
    --stage: #e9ebee;
  }
  * { margin: 0; padding: 0; box-sizing: border-box; }
  html, body { width: 1200px; height: 240px; overflow: hidden; }
  body {
    position: relative;
    background: var(--stage);
    font-family: "Open Sans", Arial, sans-serif;
    color: var(--ink);
  }
  .piece {
    position: absolute;
    background: var(--paper);
    overflow: hidden;
    box-shadow: 0 1px 3px rgba(0,0,0,.18);
  }
  .piece svg.band { position: absolute; left: 0; bottom: 0; width: 100%; }
  .wordmark {
    position: absolute;
    font-weight: 700;
    color: var(--navy);
    white-space: nowrap;
    line-height: 1;
  }
  .brand-dot {
    display: inline-block;
    border-radius: 50%;
    background: var(--sky);
    vertical-align: middle;
  }
  .wash {
    position: absolute;
    background: linear-gradient(135deg, var(--mist), rgba(230,236,245,0));
  }
  .small-text {
    position: absolute;
    font-size: 3px;
    color: var(--grey);
    line-height: 1.4;
    white-space: nowrap;
  }

  /* Business cards */
  .card .wordmark { font-size: 5px; }
  .card--dark { background: var(--ink); }
  .card--navy { background: linear-gradient(160deg, var(--blue), var(--navy)); }
  .card--dark .wordmark, .card--navy .wordmark { color: var(--paper); }

  /* Letterhead */
  .letterhead { width: 160px; height: 222px; top: 8px; }
  .letterhead .wordmark { font-size: 12px; top: 12px; right: 12px; }
  .letterhead .wash { left: 0; top: 40px; width: 110px; height: 110px; }

  /* Envelopes */
  .envelope { width: 132px; height: 54px; }
  .envelope--back { background: var(--ink); }

  /* Folder */
  .folder { top: 6px; height: 228px; }
  .folder--inside { left: 722px; width: 226px; background: linear-gradient(90deg, var(--mist), var(--paper)); }
  .folder--cover {
    left: 950px; width: 240px;
    background: radial-gradient(circle at 90% 60%, var(--blue) 0%, var(--navy) 60%, #081c40 100%);
  }
  .folder--cover .wordmark { font-size: 18px; left: 60px; top: 42px; color: var(--paper); }
</style>
</head>
<body>

<!-- Business cards, left column -->
<div class="piece card card--navy" style="left:6px;top:8px;width:40px;height:52px;"></div>
<div class="piece card" style="left:6px;top:70px;width:50px;height:40px;">
  <span class="wordmark" style="left:4px;top:6px;">Morvale Telecom</span>
  <p class="small-text" style="left:4px;top:15px;">Colin Pradwell<br>Managing Partner</p>
  <svg class="band" viewBox="0 0 50 10" height="10" preserveAspectRatio="none"><path d="M0 6 Q25 0 50 4 V10 H0Z" fill="var(--navy)"/></svg>
</div>
<div class="piece card card--dark" style="left:6px;top:120px;width:50px;height:44px;">
  <span class="wordmark" style="left:5px;top:19px;">Morvale Telecom</span>
</div>
<div class="piece card" style="left:6px;top:174px;width:50px;height:48px;">
  <div class="wash" style="left:0;top:0;width:30px;height:48px;"></div>
  <p class="small-text" style="left:9px;top:22px;">www.morvaletel.com</p>
</div>

<!-- Letterheads -->
<div class="piece letterhead" style="left:68px;">
  <span class="wordmark">Morvale Telecom</span>
  <div class="wash"></div>
  <p class="small-text" style="left:12px;bottom:26px;">87 Larkmont Suite:2261 NY, NY 10017 · www.morvaletel.com</p>
  <svg class="band" viewBox="0 0 160 22" height="22" preserveAspectRatio="none"><path d="M0 14 Q80 2 160 10 V22 H0Z" fill="var(--blue)"/><path d="M0 18 Q80 8 160 14 V22 H0Z" fill="var(--navy)"/></svg>
</div>
<div class="piece letterhead" style="left:240px;">
  <span class="wordmark">Morvale Telecom</span>
  <div class="wash"></div>
  <p class="small-text" style="left:12px;bottom:26px;">87 Larkmont Suite:2261 NY, NY 10017 · www.morvaletel.com</p>
  <svg class="band" viewBox="0 0 160 22" height="22" preserveAspectRatio="none"><path d="M0 14 Q80 2 160 10 V22 H0Z" fill="var(--blue)"/><path d="M0 18 Q80 8 160 14 V22 H0Z" fill="var(--navy)"/></svg>
</div>

<!-- Business card front and back -->
<div class="piece card" style="left:440px;top:40px;width:56px;height:32px;">
  <span class="wordmark" style="left:4px;top:5px;">Morvale Telecom</span>
  <p class="small-text" style="left:4px;top:13px;">Colin Pradwell · Managing Partner<br>cp@morvaletel.com</p>
  <svg class="band" viewBox="0 0 56 6" height="6" preserveAspectRatio="none"><path d="M0 3 Q28 0 56 2 V6 H0Z" fill="var(--navy)"/></svg>
</div>
<div class="piece card" style="left:500px;top:40px;width:46px;height:32px;">
  <div class="wash" style="left:0;top:0;width:46px;height:32px;"></div>
  <p class="small-text" style="left:8px;top:14px;">www.morvaletel.com</p>
</div>

<!-- Compliment slip -->
<div class="piece" style="left:440px;top:120px;width:106px;height:46px;">
  <span class="wordmark" style="left:6px;top:6px;font-size:7px;">Morvale Telecom</span>
  <p class="small-text" style="left:6px;top:17px;">87 Larkmont Suite:2261 NY, NY 10017</p>
  <svg class="band" viewBox="0 0 106 10" height="10" preserveAspectRatio="none"><path d="M0 6 Q53 0 106 4 V10 H0Z" fill="var(--navy)"/></svg>
</div>

<!-- Envelopes -->
<div class="piece envelope" style="left:560px;top:44px;">
  <span class="wordmark" style="left:6px;top:6px;font-size:7px;">Morvale Telecom</span>
  <p class="small-text" style="left:6px;top:16px;">87 Larkmont Suite:2261 NY, NY 10017</p>
  <svg class="band" viewBox="0 0 132 12" height="12" preserveAspectRatio="none"><path d="M0 8 Q66 0 132 5 V12 H0Z" fill="var(--navy)"/></svg>
</div>
<div class="piece envelope envelope--back" style="left:560px;top:108px;height:40px;">
  <svg viewBox="0 0 132 40" width="132" height="40"><path d="M0 0 L66 24 L132 0" fill="none" stroke="#444" stroke-width="1"/><circle cx="66" cy="22" r="4" fill="var(--blue)"/></svg>
</div>
<div class="piece envelope" style="left:560px;top:160px;">
  <svg viewBox="0 0 132 54" width="132" height="54"><path d="M0 0 L66 26 L132 0" fill="none" stroke="#c8ccd3" stroke-width="1"/><path d="M0 54 L50 24 M132 54 L82 24" stroke="#d6d9de" stroke-width="1"/><circle cx="66" cy="24" r="3" fill="var(--blue)"/></svg>
</div>

<!-- Presentation folder -->
<div class="piece folder folder--inside">
  <svg viewBox="0 0 226 228" width="226" height="228" preserveAspectRatio="none">
    <path d="M0 150 Q113 120 226 140 V228 H0Z" fill="var(--navy)"/>
    <path d="M0 150 Q113 120 226 140" fill="none" stroke="var(--sky)" stroke-width="2"/>
    <rect x="150" y="160" width="40" height="22" fill="var(--paper)"/>
  </svg>
</div>
<div class="piece folder folder--cover">
  <span class="wordmark">Morvale Telecom <span class="brand-dot" style="width:8px;height:8px;"></span></span>
</div>

</body>
</html>
```